Webbanner-Design für Führungskräfte-Coach
Danke für Ihr Engagement und die einwandfreie Abwicklung.
Zielgruppe
Ich coache Führungskräfte und Teams im Verkauf. Haupt-Keywort und Haupt-Thema:
Führung im Vertrieb. Das Design soll Führungskräften mit Verkaufsfunktionen gefallen.
Aufgabenstellung
Gemäss Memo (Datei: RBF-Banner-Memo).

```html
<!DOCTYPE html>
<html lang="de">
<head>
<meta charset="utf-8">
<title>Hessberg Coaching &amp; Training – Seite</title>
<link rel="stylesheet" href="https://fonts.googleapis.com/css2?family=Arimo:wght@400;700&family=Open+Sans:wght@400;600&family=Roboto+Condensed:wght@400&display=swap">
<style>
:root{
  --bar:#3b5998;
  --page:#e9ebee;
  --card:#ffffff;
  --line:#dddfe2;
  --text:#1d2129;
  --muted:#90949c;
  --icon:#8d949e;
  --link:#365899;
  --accent:#4080ff;
  --placeholder:#5b8ff9;
  --green:#42b72a;
  --avatar:#7b6455;
}
*{box-sizing:border-box;margin:0;padding:0}
html,body{width:900px;height:1200px;overflow:hidden;background:var(--page);font-family:"Arimo",Arial,sans-serif;color:var(--text);font-size:9px}
.canvas{position:relative;width:900px;height:1200px}
.abs{position:absolute}
.ico{display:inline-block;vertical-align:middle;fill:currentColor}
.topbar{left:0;top:0;width:900px;height:29px;background:var(--bar)}
.topbar .brand-square{left:99px;top:5px;width:17px;height:17px;background:#fff;border-radius:2px}
.topbar .search{left:122px;top:5px;width:296px;height:16px;background:#fff;border-radius:2px;padding:3px 7px;font-size:9px}
.topbar .search .ico{position:absolute;right:8px;top:3px;color:#777}
.topbar .user{left:550px;top:6px;color:#fff;font-weight:700;font-size:8px;display:flex;align-items:center;gap:4px}
.topbar .user i{display:inline-block;width:13px;height:14px;background:var(--avatar)}
.topbar .user .home{margin-left:10px}
.topbar .nav-icons{left:666px;top:7px;display:flex;gap:9px;color:#fff}
.topbar .nav-icons .sep{width:1px;height:14px;background:rgba(255,255,255,.25);margin:0 4px}
.card{position:absolute;background:var(--card);border:1px solid var(--line);border-radius:2px}
.profile-photo{left:100px;top:43px;width:106px;height:104px;background:linear-gradient(#e6e8ec,#9aa6b8 55%,#2b2e34);border:3px solid #fff;box-shadow:0 0 0 1px var(--line)}
.page-name{left:99px;top:163px;width:117px;font-family:"Roboto Condensed","Arial Narrow",sans-serif;font-size:10px;color:#333;white-space:nowrap}
.verified{left:139px;top:178px;width:13px;height:13px}
.handle{left:100px;top:195px;font-size:9px;color:var(--muted)}
.side-nav{left:99px;top:219px;width:117px;list-style:none}
.side-nav li{height:21.3px;line-height:21px;padding-left:7px;font-size:9.5px;color:#4b4f56}
.side-nav li.active{background:#e4e6ea;border-left:2px solid var(--bar);color:var(--text);font-weight:600}
.create-btn{left:104px;top:379px;width:66px;height:16px;background:var(--green);color:#fff;font-weight:700;font-size:7.5px;text-align:center;line-height:16px;border-radius:2px}
.cover{left:221px;top:29px;width:552px;height:208px;background:linear-gradient(90deg,#8ea3b9,#c7ced6 40%,#7d8a99 70%,#4c5867)}
.cover-band{left:221px;top:45px;width:552px;height:40px;background:rgba(230,232,238,.85)}
.cover-logo{left:277px;top:53px;display:flex;align-items:center;gap:6px}
.cover-logo .mark{width:22px;height:22px;background:#4a5968}
.cover-logo b{display:block;font-size:12px;color:#222}
.cover-logo span{font-size:9px;color:#555}
.cover-tagline{left:221px;top:187px;width:552px;height:25px;background:rgba(210,214,222,.75);text-align:center;line-height:25px;font-family:"Open Sans",sans-serif;font-size:12px;color:#111}
.action-bar{left:221px;top:237px;width:552px;height:35px;background:var(--card);border:1px solid var(--line);border-top:none}
.btn-group{left:230px;top:245px;display:flex;border:1px solid #ccd0d5;border-radius:2px;background:#f6f7f9}
.btn-group span{padding:3px 7px;font-size:7.5px;font-weight:700;color:#4b4f56;border-right:1px solid #ccd0d5;display:flex;align-items:center;gap:3px}
.btn-group span:last-child{border:none}
.contact-btn{left:566px;top:246px;width:198px;height:18px;background:var(--accent);color:#fff;font-size:9.5px;text-align:center;line-height:18px;border-radius:2px}
.avatar{background:var(--avatar);border-radius:1px}
.composer{left:221px;top:282px;width:335px;height:71px}
.composer .tabs{height:22px;border-bottom:1px solid var(--line);background:#f6f7f9;padding:0 12px;font-size:8px;color:#4b4f56;display:flex;align-items:center;gap:5px}
.composer .tabs a{color:var(--link);text-decoration:none}
.composer .tabs .right{margin-left:auto;display:flex;align-items:center;gap:3px}
.composer .prompt{position:absolute;left:42px;top:38px;color:#b3a5a0;font-size:9px}
.post-head{position:absolute;left:8px;top:8px;display:flex;gap:8px}
.post-head .avatar{width:24px;height:26px}
.post-head .who{font-size:7.5px;color:#4b4f56;line-height:1.4}
.post-head .who b{font-weight:400;font-size:10px;color:var(--link)}
.post-head .who a{color:var(--link);text-decoration:none}
.post-head .time{color:var(--muted);font-size:7.5px}
.chev{position:absolute;right:12px;top:14px;width:6px;height:6px;border-right:1px solid #aaa;border-bottom:1px solid #aaa;transform:rotate(45deg)}
.mini-cover{position:absolute;left:8px;width:320px;background:linear-gradient(90deg,#8ea3b9,#c7ced6 40%,#7d8a99 70%,#4c5867)}
.mini-cover .band{position:absolute;left:0;top:12px;right:0;height:22px;background:rgba(230,232,238,.85);padding:4px 32px;font-size:5px;color:#444;display:flex;gap:4px;align-items:center}
.mini-cover .band i{width:12px;height:12px;background:#4a5968}
.mini-cover .band b{font-size:7px;color:#222;display:block}
.mini-cover .tag{position:absolute;left:0;right:0;bottom:10px;height:14px;background:rgba(210,214,222,.75);font-size:6.5px;text-align:center;line-height:14px;font-family:"Open Sans",sans-serif}
.post-image{position:absolute;left:8px;width:320px;background:var(--placeholder)}
.post-actions{position:absolute;left:0;right:0;height:24px;border-top:1px solid var(--line);border-bottom:1px solid var(--line);padding:0 11px;font-size:8px;color:#4b4f56;display:flex;align-items:center;gap:22px}
.post-actions span{display:flex;align-items:center;gap:5px}
.post-actions .ico{color:var(--icon)}
.post-actions .avatar{position:absolute;right:9px;top:6px;width:12px;height:12px}
.reactions{position:absolute;left:8px;right:8px;display:flex;justify-content:space-between;align-items:center;font-size:8px;color:var(--link)}
.reactions .dots{display:flex;align-items:center}
.reactions .dots svg{margin-right:-1px}
.comment-row{position:absolute;left:8px;right:8px;display:flex;gap:6px}
.comment-row .avatar{width:20px;height:20px}
.comment-row .field{flex:1;border:1px solid var(--line);border-radius:2px;height:22px;padding:0 8px;color:#a7abb1;font-size:8.5px;display:flex;align-items:center}
.comment-row .field .tools{margin-left:auto;display:flex;gap:8px;color:#a7abb1}
.post-body{position:absolute;left:8px;right:20px;font-size:8px;line-height:1.45}
.side-card{position:absolute;left:565px;width:208px;background:var(--card);border:1px solid var(--line);border-radius:2px}
.side-title{height:22px;border-bottom:1px solid var(--line);padding:7px 6px;font-size:7.5px;color:#4b4f56;position:relative}
.side-title::after{content:"";position:absolute;right:10px;top:8px;width:5px;height:5px;border-right:1.5px solid #555;border-top:1.5px solid #555;transform:rotate(45deg)}
.photo-grid{display:grid;grid-template-columns:repeat(3,64px);grid-auto-rows:60px;gap:4px;padding:3px 3px 0 4px}
.photo-grid div{background:var(--placeholder)}
.video-main{position:absolute;left:4px;top:25px;width:200px;height:98px;background:linear-gradient(var(--placeholder) 75%,#2f5fcf)}
.video-small{position:absolute;top:129px;width:98px;height:59px;background:linear-gradient(var(--placeholder) 60%,#2f5fcf)}
.stats{position:absolute;bottom:5px;left:6px;right:6px;color:#fff;font-size:7px;font-weight:700;display:flex;justify-content:space-between;align-items:center}
.stats span{display:flex;align-items:center;gap:2px}
.video-main .stats{left:auto;gap:8px}
</style>
</head>
<body>
<svg width="0" height="0" style="position:absolute">
  <defs>
    <symbol id="i-like" viewBox="0 0 12 12"><path d="M1 5h2.5v6H1zM4.3 5l2.3-4c.8 0 1.3.6 1.1 1.5L7.3 4.5h3c.7 0 1.1.6.9 1.2l-1.2 4.5c-.2.5-.6.8-1.1.8H4.3z"/></symbol>
    <symbol id="i-comment" viewBox="0 0 12 12"><path d="M1 2h10v6.5H5L2.5 11V8.5H1z"/></symbol>
    <symbol id="i-share" viewBox="0 0 12 12"><path d="M7 1.5l4.5 4-4.5 4V7.3C4 7.3 2.2 8.3 1 10.5c.4-3.6 2.4-5.8 6-6.2z"/></symbol>
    <symbol id="i-camera" viewBox="0 0 12 12"><path d="M1 3.5h2.2l1-1.5h3.6l1 1.5H11V10H1zM6 4.5a2.2 2.2 0 100 4.4 2.2 2.2 0 000-4.4z" fill-rule="evenodd"/></symbol>
    <symbol id="i-smile" viewBox="0 0 12 12"><circle cx="6" cy="6" r="5" fill="none" stroke="currentColor" stroke-width="1"/><circle cx="4.3" cy="4.8" r=".7"/><circle cx="7.7" cy="4.8" r=".7"/><path d="M3.8 7.2c1.2 1.5 3.2 1.5 4.4 0" fill="none" stroke="currentColor" stroke-width=".9"/></symbol>
    <symbol id="i-search" viewBox="0 0 12 12"><circle cx="5" cy="5" r="3.6" fill="none" stroke="currentColor" stroke-width="1.4"/><path d="M7.6 7.6l3.2 3.2" stroke="currentColor" stroke-width="1.6"/></symbol>
    <symbol id="i-pencil" viewBox="0 0 12 12"><path d="M8.5 1l2.5 2.5L4.5 10 1.5 11l1-3z"/></symbol>
    <symbol id="i-people" viewBox="0 0 16 12"><circle cx="5.5" cy="3.5" r="2.6"/><path d="M.5 11.5c0-3 2.2-4.8 5-4.8s5 1.8 5 4.8z"/><circle cx="11.5" cy="3" r="2.2"/><path d="M11 6.3c2.6 0 4.5 1.6 4.5 4.4h-3.6c0-1.8-.5-3.3-1.5-4.4z"/></symbol>
    <symbol id="i-chat" viewBox="0 0 16 12"><path d="M4 1h11v7h-2v2.5L10.5 8H4z"/><path d="M1 4h2v5h5.5L7 10.5H4L1.5 12V10.5H1z"/></symbol>
    <symbol id="i-globe" viewBox="0 0 12 12"><circle cx="6" cy="6" r="5.5"/><path d="M3 2.5c1.5.5 1 2 2.5 2.2S6 7 4.5 7.5 3.5 10 3.8 10.5M7.5 1.2C7 2.5 8.5 3 9.5 3.2s1.2 2.3.3 3.2-.3 2.5.6 2.8" fill="none" stroke="#3b5998" stroke-width=".9"/></symbol>
    <symbol id="i-menu" viewBox="0 0 14 12"><path d="M1 2h5v4H1zM7.5 2.5H13M7.5 4.5H13M1 8h12M1 10h12" stroke="currentColor" stroke-width="1.2" fill="none"/></symbol>
    <symbol id="i-caret" viewBox="0 0 8 6"><path d="M0 1h8L4 5.5z"/></symbol>
    <symbol id="i-dots" viewBox="0 0 12 4"><circle cx="2" cy="2" r="1"/><circle cx="6" cy="2" r="1"/><circle cx="10" cy="2" r="1"/></symbol>
    <symbol id="i-addperson" viewBox="0 0 14 12"><circle cx="5" cy="3.5" r="2.6"/><path d="M0 11.5c0-3 2.2-4.8 5-4.8s5 1.8 5 4.8z"/><path d="M11 3v5M8.5 5.5h5" stroke="currentColor" stroke-width="1.4"/></symbol>
    <symbol id="i-info" viewBox="0 0 12 12"><circle cx="6" cy="6" r="5.5"/><path d="M6 5.2v3.8M6 3v.9" stroke="#fff" stroke-width="1.3"/></symbol>
    <symbol id="i-play" viewBox="0 0 12 12"><path d="M3 1.5l7.5 4.5L3 10.5z"/></symbol>
  </defs>
</svg>
<div class="canvas">

  <header class="abs topbar">
    <div class="abs brand-square"></div>
    <div class="abs search">PagePress.net<svg class="ico" width="10" height="10"><use href="#i-search"/></svg></div>
    <div class="abs user"><i></i>John Smith<span class="home">Home</span></div>
    <div class="abs nav-icons">
      <svg class="ico" width="15" height="13"><use href="#i-people"/></svg>
      <svg class="ico" width="15" height="13"><use href="#i-chat"/></svg>
      <svg class="ico" width="13" height="13"><use href="#i-globe"/></svg>
      <span class="sep"></span>
      <svg class="ico" width="12" height="11"><use href="#i-menu"/></svg>
      <svg class="ico" width="7" height="6" style="margin-left:-4px;margin-top:3px"><use href="#i-caret"/></svg>
    </div>
  </header>

  <aside>
    <div class="abs profile-photo" role="img" aria-label="Porträtfoto des Coaches im dunklen Sakko"></div>
    <div class="abs page-name">Coaching &amp; Training GmbH</div>
    <svg class="abs verified" viewBox="0 0 13 13"><circle cx="6.5" cy="6.5" r="6.5" fill="#4080ff"/><path d="M3.5 6.8l2 2 4-4.2" stroke="#fff" stroke-width="1.5" fill="none"/></svg>
    <div class="abs handle">@PagePress</div>
    <ul class="abs side-nav">
      <li class="active">Home</li><li>Photos</li><li>Likes</li><li>About</li><li>Videos</li><li>Welcome</li><li>Posts</li>
    </ul>
    <div class="abs create-btn">Create a Page</div>
  </aside>

  <section>
    <div class="abs cover" role="img" aria-label="Titelbild: Coach im Vordergrund, Team von Führungskräften unscharf im Hintergrund"></div>
    <div class="abs cover-band"></div>
    <div class="abs cover-logo"><div class="mark"></div><div><b>Hessberg</b><span>Coaching &amp; Training GmbH</span></div></div>
    <div class="abs cover-tagline">Coach für Führungskräfte und Teams im Vertrieb</div>
    <div class="abs action-bar"></div>
    <div class="abs btn-group">
      <span><svg class="ico" width="9" height="9" style="color:var(--link)"><use href="#i-like"/></svg>Liked<svg class="ico" width="6" height="5"><use href="#i-caret"/></svg></span>
      <span><svg class="ico" width="9" height="9" style="color:var(--icon)"><use href="#i-comment"/></svg>Message</span>
      <span><svg class="ico" width="9" height="3" style="color:var(--icon)"><use href="#i-dots"/></svg>More<svg class="ico" width="6" height="5"><use href="#i-caret"/></svg></span>
    </div>
    <div class="abs contact-btn">Contact Us</div>
  </section>

  <main>
    <div class="card composer">
      <div class="tabs">
        <svg class="ico" width="9" height="9" style="color:#5b7bd5"><use href="#i-pencil"/></svg>Status
        <svg class="ico" width="10" height="9" style="color:var(--icon);margin-left:6px"><use href="#i-camera"/></svg><a>Photo / Video</a>
        <span class="right"><i class="avatar" style="width:11px;height:11px;display:inline-block"></i><svg class="ico" width="6" height="5" style="color:#606770"><use href="#i-caret"/></svg></span>
      </div>
      <div class="avatar" style="position:absolute;left:8px;top:30px;width:27px;height:27px"></div>
      <div class="prompt">Write something on this Page...</div>
    </div>

    <article class="card" style="left:221px;top:361px;width:335px;height:264px">
      <div class="post-head"><div class="avatar"></div><div class="who"><b>PagePress.net</b> changed their <a>cover photo.</a><br><span class="time">2 mins</span></div></div>
      <div class="chev"></div>
      <div class="mini-cover" role="img" aria-label="Neues Titelbild: Coach vor seinem Team" style="top:46px;height:122px">
        <div class="band"><i></i><div><b>Hessberg</b>Coaching &amp; Training GmbH</div></div>
        <div class="tag">Coach für Führungskräfte und Teams im Vertrieb</div>
      </div>
      <div class="post-actions" style="top:176px">
        <span><svg class="ico" width="10" height="10"><use href="#i-like"/></svg>Like</span>
        <span><svg class="ico" width="10" height="10"><use href="#i-comment"/></svg>Comment</span>
        <span><svg class="ico" width="10" height="10"><use href="#i-share"/></svg>Share</span>
        <div class="avatar"></div>
      </div>
      <div class="reactions" style="top:212px">
        <span class="dots">
          <svg width="11" height="11" viewBox="0 0 12 12"><circle cx="6" cy="6" r="5.5" fill="#4080ff" stroke="#fff"/><use href="#i-like" x="3" y="3" width="6" height="6" fill="#fff"/></svg>
          <svg width="11" height="11" viewBox="0 0 12 12"><circle cx="6" cy="6" r="5.5" fill="#f25268" stroke="#fff"/><path d="M6 9L3.3 6.2a1.5 1.5 0 012.7-2 1.5 1.5 0 012.7 2z" fill="#fff"/></svg>
          <svg width="11" height="11" viewBox="0 0 12 12"><circle cx="6" cy="6" r="5.5" fill="#f7b928" stroke="#fff"/><circle cx="4.3" cy="4.8" r=".8" fill="#5a3a10"/><circle cx="7.7" cy="4.8" r=".8" fill="#5a3a10"/><ellipse cx="6" cy="8" rx="1.2" ry="1.4" fill="#5a3a10"/></svg>
          &nbsp;1.6M</span>
        <span>Top Comments <svg class="ico" width="5" height="4"><use href="#i-caret"/></svg></span>
      </div>
      <div class="comment-row" style="top:234px"><div class="avatar"></div><div class="field">Write a comment...<span class="tools"><svg class="ico" width="11" height="10"><use href="#i-camera"/></svg><svg class="ico" width="10" height="10"><use href="#i-smile"/></svg></span></div></div>
    </article>

    <article class="card" style="left:221px;top:633px;width:335px;height:529px">
      <div class="post-head"><div class="avatar"></div><div class="who"><b>PagePress.net</b> changed their <a>cover photo.</a><br><span class="time">June 17</span></div></div>
      <div class="chev"></div>
      <div class="post-body" style="top:48px">Lorem ipsum dolor sit amet timeti ergo sum Lorem ipsum dolor sit amet timeti dolor sit amet timeti imeti ergo sum imeti ergo sum</div>
      <div class="post-image" role="img" aria-label="Beitragsbild" style="top:81px;height:320px"></div>
      <div class="post-actions" style="top:412px">
        <span><svg class="ico" width="10" height="10"><use href="#i-like"/></svg>Like</span>
        <span><svg class="ico" width="10" height="10"><use href="#i-comment"/></svg>Comment</span>
        <span><svg class="ico" width="10" height="10"><use href="#i-share"/></svg>Share</span>
        <div class="avatar"></div>
      </div>
      <div class="reactions" style="top:445px">
        <span class="dots">
          <svg width="11" height="11" viewBox="0 0 12 12"><circle cx="6" cy="6" r="5.5" fill="#4080ff" stroke="#fff"/><use href="#i-like" x="3" y="3" width="6" height="6" fill="#fff"/></svg>
          <svg width="11" height="11" viewBox="0 0 12 12"><circle cx="6" cy="6" r="5.5" fill="#f25268" stroke="#fff"/><path d="M6 9L3.3 6.2a1.5 1.5 0 012.7-2 1.5 1.5 0 012.7 2z" fill="#fff"/></svg>
          <svg width="11" height="11" viewBox="0 0 12 12"><circle cx="6" cy="6" r="5.5" fill="#f7b928" stroke="#fff"/><circle cx="4.3" cy="4.8" r=".8" fill="#5a3a10"/><circle cx="7.7" cy="4.8" r=".8" fill="#5a3a10"/><ellipse cx="6" cy="8" rx="1.2" ry="1.4" fill="#5a3a10"/></svg>
          &nbsp;1.6M</span>
        <span>Top Comments <svg class="ico" width="5" height="4"><use href="#i-caret"/></svg></span>
      </div>
      <div class="reactions" style="top:473px"><span>11,397 shares</span><span style="color:var(--muted)">15K Comments</span></div>
      <div class="comment-row" style="top:497px"><div class="avatar"></div><div class="field">Write a comment...<span class="tools"><svg class="ico" width="11" height="10"><use href="#i-camera"/></svg><svg class="ico" width="10" height="10"><use href="#i-smile"/></svg></span></div></div>
    </article>
  </main>

  <aside>
    <div class="side-card" style="top:282px;height:28px;padding:8px 8px;font-size:9.5px">Personal Website</div>
    <div class="side-card" style="top:318px;height:25px;padding:0 8px;font-size:9px;color:var(--muted);display:flex;align-items:center;gap:7px"><svg class="ico" width="10" height="10" style="color:var(--icon)"><use href="#i-search"/></svg>Search for Posts on the Page</div>
    <div class="side-card" style="top:352px;height:66px">
      <div class="avatar" style="position:absolute;left:9px;top:4px;width:19px;height:23px"></div>
      <div style="position:absolute;left:34px;top:5px;font-size:8px;line-height:1.6">1,955.550 people like this<br><span style="color:var(--muted)">Tom Smith and 20 other friends</span></div>
      <div style="position:absolute;left:0;right:0;top:32px;border-top:1px solid var(--line)"></div>
      <svg class="ico" width="13" height="11" style="position:absolute;left:12px;top:44px;color:#bec3c9"><use href="#i-addperson"/></svg>
      <div style="position:absolute;left:36px;top:45px;font-size:7.5px;color:#4b4f56">Invite friends to like this Page</div>
    </div>
    <div class="side-card" style="top:427px;height:90px">
      <div class="side-title">ABOUT</div>
      <svg class="ico" width="7" height="7" style="position:absolute;left:9px;top:35px;color:#ccd0d5"><use href="#i-info"/></svg>
      <div style="padding:10px 8px 0 22px;font-size:7.8px;line-height:1.45">Lorem ipsum dolor sit amet timeti ergo sum Lorem ipsum dolor sit amet timeti dolor sit amet timeti imeti ergo sum imeti ergo sum</div>
      <svg class="ico" width="7" height="7" style="position:absolute;left:9px;top:79px;color:#ccd0d5"><use href="#i-globe"/></svg>
      <div style="padding:6px 0 0 22px;font-size:7.5px;color:var(--link)">http://www.pagepress.net/</div>
    </div>
    <div class="side-card" style="top:527px;height:215px">
      <div class="side-title">PHOTOS</div>
      <div class="photo-grid" role="img" aria-label="Fotogalerie mit neun Bildern">
        <div></div><div></div><div></div><div></div><div></div><div></div><div></div><div></div><div></div>
      </div>
    </div>
    <div class="side-card" style="top:753px;height:192px">
      <div class="side-title">VIDEOS</div>
      <div class="video-main" role="img" aria-label="Videovorschau">
        <svg style="position:absolute;left:74px;top:23px" width="56" height="56" viewBox="0 0 56 56"><circle cx="28" cy="28" r="26" fill="none" stroke="#fff" stroke-width="2"/><path d="M22 18l16 10-16 10z" fill="#fff"/></svg>
        <div class="stats"><span><svg class="ico" width="9" height="9"><use href="#i-like"/></svg>139K</span><span><svg class="ico" width="9" height="9"><use href="#i-comment"/></svg>2.2K</span></div>
      </div>
      <div class="video-small" role="img" aria-label="Videovorschau" style="left:4px"><div class="stats"><span><svg class="ico" width="9" height="9"><use href="#i-like"/></svg>139K</span><span><svg class="ico" width="9" height="9"><use href="#i-comment"/></svg>2.2K</span></div></div>
      <div class="video-small" role="img" aria-label="Videovorschau" style="left:106px"><div class="stats"><span><svg class="ico" width="9" height="9"><use href="#i-like"/></svg>139K</span><span><svg class="ico" width="9" height="9"><use href="#i-comment"/></svg>2.2K</span></div></div>
    </div>
  </aside>

</div>
</body>
</html>
```